ROOFING SALES QUOTE TEMPLATE / BROCHURE

I am a roofing contractor looking to elevate and simplify the sales presentation of our roof installation services to our customers through a slick/company branded bid form or brochure. Im looking more for design elements in a template format that can be used/modified to have information populated based on unique customer needs.
I would like to have the bid form or brochure present 3 options to homeowners: GOOD / BETTER / BEST

Potentially include pages with details to educate the homeowners on the components of a roof, the material /product specifications included in each of the GOOD/BETTER/BEST options, our insurance information, licensing, etc.

For example: Homeowner Dorian is looking to have his asphalt shingle roof replaced on his residential home. Dorian knows nothing about roofing, but knows the roof is getting old.
Bramblet Roofing would like to present him with three replacement options, with different price points:
OPTION 1 (Good) = Remove and replace existing roof with new shingle tier 1 quality
OPTION 2 (BETTER) = remove and replace existing roof with new shingle tier 2 quality and better warranty
OPTION 3 (BEST) = remove and replace existing roof with new highest quality shingle and highest grade warranty

I would like one page to concisely present all three options, visually simple with price, and option summaries

One page which essentially educates on the components of a roof (attic space, trusses/rafters/eaves , plywood decking, roofing felts/underlayment, shingle material, metal flashings, ridge and hip shingles, ventilation, etc) -graphic?

One or more pages that show more specific details/scope of each of the options presented (unless this is TMI and we can provide a URL

Another page showcasing our license, insurance, bonds, certification, etc.

For branding, we are partnered with the manufacturer KLO in case we can co-brand anything.

Most of these will be used electronically and filled out as a PDF or similar.

Target Market(s)

Residential and commercial building owners looking for roof replacements

Industry/Entity Type

Roofing (USA - California)

Requirements
Must have
• present 3 options to homeowners: GOOD / BETTER / BEST -design must match logo colors
Nice to have
• One or more pages that show more specific details/scope of each of the options presented (unless this is TMI and we can provide a URL
Should not have
• too much wordiness

```html
<!DOCTYPE html>
<html lang="en">
<head>
<meta charset="utf-8">
<title>Bramblet Roofing – Choose Your Roof</title>
<link rel="stylesheet" href="https://fonts.googleapis.com/css2?family=Anton&family=Oswald:wght@600&family=Montserrat:wght@800;900&display=swap">
<style>
  :root{
    --orange:#f26b38;
    --ink:#1e1d1f;
    --charcoal:#2a2a2c;
    --white:#ffffff;
    --roof-grey:#6e6b70;
  }
  *{box-sizing:border-box;margin:0;padding:0}
  html,body{width:873px;height:1200px;overflow:hidden;background:var(--white)}
  .sheet{position:relative;width:873px;height:1200px;overflow:hidden;background:var(--white);font-family:"Montserrat",Arial,sans-serif}

  /* hero */
  .hero{position:absolute;left:0;top:0;width:873px;height:521px}
  .hero-photo{position:absolute;inset:0;
    background:linear-gradient(160deg,#c9c6c0 0%,#9c9488 35%,#7d776f 55%,#6f6c72 75%,var(--roof-grey) 100%)}
  .hero-shapes{position:absolute;inset:0}
  .hero-rule{position:absolute;left:0;top:521px;width:873px;height:15px;background:var(--ink)}

  .brand{position:absolute;left:61px;top:74px;width:157px;text-align:center;
    font-family:"Oswald",Arial,sans-serif;font-weight:600;color:var(--white);
    font-size:30px;line-height:1.05;letter-spacing:.5px}

  .headline{position:absolute;right:58px;top:206px;text-align:right;
    font-family:"Anton",Impact,sans-serif;color:var(--orange);
    text-shadow:2px 3px 6px rgba(0,0,0,.45);line-height:1}
  .headline .big{display:block;font-size:122px;letter-spacing:-1px}
  .headline .mid{display:block;font-size:88px;margin-top:8px}
  .tiers-line{position:absolute;right:64px;top:436px;
    font-family:"Montserrat",Arial,sans-serif;font-weight:900;font-size:33px;color:var(--charcoal);letter-spacing:.5px}

  /* options */
  .options{position:absolute;left:50px;top:596px;width:773px;height:445px;display:flex;gap:35px}
  .option{position:relative;width:234px;height:445px;background:var(--ink);padding:0 10px 10px}
  .option-title{height:70px;display:flex;align-items:center;justify-content:center;
    color:var(--white);font-weight:900;font-size:31px;letter-spacing:.5px}
  .option-photo{height:207px}
  .photo-silver{background:linear-gradient(160deg,#c9d2d6 0%,#8a5a52 30%,#3d3a3f 55%,#2e2c30 100%)}
  .photo-gold{background:linear-gradient(160deg,#5d97c3 0%,#7aa9cc 40%,#c8c96a 70%,#3f6f8c 100%)}
  .photo-platinum{background:linear-gradient(160deg,#dfe6ec 0%,#b9c4cc 35%,#4d5058 65%,#2f3137 100%)}
  .option-text{height:158px;background:var(--white);padding-top:20px;text-align:center;
    color:var(--charcoal);font-weight:800;font-size:16px;line-height:22px;letter-spacing:.2px}

  .badge{position:absolute;top:95px;width:104px;height:104px;border-radius:50%;background:var(--orange);
    display:flex;align-items:center;justify-content:center;text-align:center;
    font-family:"Oswald",Arial,sans-serif;font-weight:600;color:var(--white);font-size:17px;line-height:1.2}
  .badge-gold{left:159px}
  .badge-platinum{left:174px;font-size:16.5px}

  /* contact */
  .contact{position:absolute;left:0;top:1118px;width:873px;height:82px}
  .contact-bg{position:absolute;inset:0}
  .contact-label{position:absolute;left:20px;top:24px;font-weight:900;font-size:33px;color:var(--charcoal);letter-spacing:.5px}
  .phone{position:absolute;left:278px;top:26px;display:flex;align-items:center;gap:18px;
    color:var(--white);font-weight:900;font-size:30px;letter-spacing:1px}
  .links{position:absolute;left:564px;top:20px;color:var(--white);font-weight:800;font-size:16px;line-height:24px}
  .links li{list-style:none;display:flex;align-items:center;gap:20px}
</style>
</head>
<body>
<main class="sheet">

  <section class="hero">
    <div class="hero-photo" role="img" aria-label="Photo of a roofer in a hard hat sitting on a metal roof above bare winter trees and countryside"></div>
    <svg class="hero-shapes" width="873" height="521" viewBox="0 0 873 521">
      <polygon points="0,0 508,0 0,339" fill="var(--orange)"/>
      <polygon points="508,0 580,0 0,392 0,339" fill="var(--ink)"/>
    </svg>
    <div class="brand">BRAMBLET<br>ROOFING</div>
    <h1 class="headline"><span class="big">CHOOSE</span><span class="mid">YOUR ROOF</span></h1>
    <p class="tiers-line">GOOD / BETTER / BEST</p>
  </section>
  <div class="hero-rule"></div>

  <section class="options">
    <article class="option">
      <h2 class="option-title">SILVER</h2>
      <div class="option-photo photo-silver" role="img" aria-label="Photo of dark shingle tiles along a roof edge"></div>
      <p class="option-text">REMOVE AND<br>REPLACE EXISTING<br>ROOF WITH NEW<br>SHINGLE TIER 1<br>QUALITY</p>
    </article>
    <article class="option">
      <h2 class="option-title">GOLD</h2>
      <div class="option-photo photo-gold" role="img" aria-label="Photo of a roofer in a hard hat and safety vest beside a tiled roof"></div>
      <p class="option-text">REMOVE AND<br>REPLACE EXISTING<br>ROOF WITH NEW<br>SHINGLE TIER 2<br>QUALITY</p>
      <div class="badge badge-gold">BETTER<br>WARRANTY</div>
    </article>
    <article class="option">
      <h2 class="option-title">PLATINUM</h2>
      <div class="option-photo photo-platinum" role="img" aria-label="Photo of a roofer working on a dark standing-seam metal roof"></div>
      <p class="option-text">REMOVE AND<br>REPLACE EXISTING<br>ROOF WITH NEW<br>HIGHEST QUALITY<br>SHINGLE</p>
      <div class="badge badge-platinum">HIGHEST<br>GRADE<br>WARRANTY</div>
    </article>
  </section>

  <footer class="contact">
    <svg class="contact-bg" width="873" height="82" viewBox="0 0 873 82">
      <rect x="0" y="11" width="873" height="71" fill="var(--ink)"/>
      <polygon points="0,0 255,0 230,82 0,82" fill="var(--orange)"/>
    </svg>
    <p class="contact-label">CONTACT</p>
    <div class="phone">
      <svg width="24" height="24" viewBox="0 0 24 24" aria-hidden="true">
        <path d="M6.6 2.5l3 3.6-1.9 2.4c1.2 2.6 3.2 4.7 5.8 5.9l2.4-1.9 3.6 3-1.7 3.3c-.5.9-1.5 1.3-2.5 1C9 17.8 4.2 13 2.2 6.7c-.3-1 .1-2 1-2.5z" fill="var(--orange)"/>
        <path d="M14 3.5a7 7 0 0 1 6.5 6.5M14 7a3.5 3.5 0 0 1 3 3" stroke="var(--orange)" stroke-width="1.8" fill="none" stroke-linecap="round"/>
      </svg>
      <span>0000 00000</span>
    </div>
    <ul class="links">
      <li>
        <svg width="16" height="12" viewBox="0 0 16 12" aria-hidden="true"><rect x="1" y="1" width="14" height="10" fill="none" stroke="var(--orange)" stroke-width="1.6"/><path d="M1 1l7 6 7-6" fill="none" stroke="var(--orange)" stroke-width="1.6"/></svg>
        <span>brambletroofing@email.com</span>
      </li>
      <li>
        <svg width="16" height="16" viewBox="0 0 16 16" aria-hidden="true"><circle cx="8" cy="8" r="6.8" fill="none" stroke="var(--orange)" stroke-width="1.5"/><ellipse cx="8" cy="8" rx="3" ry="6.8" fill="none" stroke="var(--orange)" stroke-width="1.3"/><path d="M1.2 8h13.6M2.5 4.5h11M2.5 11.5h11" stroke="var(--orange)" stroke-width="1.2"/></svg>
        <span>www.brambletroofing.com</span>
      </li>
    </ul>
  </footer>

</main>
</body>
</html>
```